Wordpress Template for Food Retail Shop

We need a wordpress template that fits our new wp installation with about 6-7 sites. frontpage, news, team, products, contact. we provide food from local suppliers, * green * products. we provide a local bakery

```html
<!DOCTYPE html>
<html lang="en">
<head>
<meta charset="utf-8">
<title>Grana – Local Bakery</title>
<link rel="stylesheet" href="https://fonts.googleapis.com/css2?family=Poppins:wght@300;400;500;600;700&family=Great+Vibes&display=swap">
<style>
:root{
  --navy:#0f2a4a;
  --green:#75c10a;
  --olive:#7a9a0a;
  --orange:#e8921c;
  --ink:#333;
  --muted:#777;
  --topbar:#3a3a3a;
  --footer:#1f2428;
  --pale:#f6f9fb;
  --grey:#f1f2f3;
}
*{margin:0;padding:0;box-sizing:border-box}
html,body{width:1200px;height:3805px;overflow:hidden}
body{font-family:'Poppins',sans-serif;color:var(--ink);background:#fff;position:relative}
.abs{position:absolute}
.script{font-family:'Great Vibes',cursive;font-weight:400}
section,header,footer{position:absolute;left:0;width:1200px}

.topbar{top:0;height:31px;background:var(--topbar)}
.topbar .links{position:absolute;right:130px;top:8px;font-size:10px;color:#f4c400;display:flex;gap:22px}
.topbar .links span::before{content:"";display:inline-block;width:8px;height:8px;border-radius:50%;background:#f4c400;margin-right:6px;vertical-align:-1px}

.site-header{top:31px;height:105px;background:#fff}
.brand{position:absolute;left:77px;top:28px;display:flex;align-items:center;gap:10px}
.brand .mark{width:44px;height:44px;border-radius:50%;background:var(--orange)}
.brand .name{font-size:36px;font-weight:600;color:var(--green);letter-spacing:1px}
.phone{position:absolute;right:150px;top:24px;display:flex;align-items:center;gap:10px;color:var(--olive);font-size:18px;font-weight:500}
.phone .ic{width:30px;height:30px;border-radius:50%;border:1.5px solid #ccc;display:flex;align-items:center;justify-content:center}
.nav{position:absolute;top:66px;left:566px;display:flex;gap:0;font-size:14px;color:#444}
.nav a{text-decoration:none;color:inherit;margin-right:33px}
.nav a.active{color:var(--olive)}

.hero{top:136px;height:551px;background:linear-gradient(120deg,#eef1f3,#dde2e5)}
.hero .photo{position:absolute;left:649px;top:0;width:551px;height:551px;background:linear-gradient(160deg,#e9e6df,#c9b79f 60%,#8a6a45)}
.hero .loaf{position:absolute;left:0;top:420px;width:190px;height:150px;background:radial-gradient(ellipse at 35% 70%,#b77a3e,#7a4a22 60%,transparent 72%)}
.hero .kicker{position:absolute;left:149px;top:108px;font-size:50px;color:var(--olive)}
.hero h1{position:absolute;left:149px;top:160px;font-size:62px;font-weight:700;color:var(--navy);letter-spacing:-.5px}
.hero p{position:absolute;left:149px;top:246px;width:420px;font-size:15px;line-height:28px;color:#555;font-weight:300}
.btn{position:absolute;display:flex;align-items:center;justify-content:center;border-radius:30px;font-weight:500;text-decoration:none}
.hero .btn{left:149px;top:322px;width:175px;height:55px;background:var(--olive);color:#fff;font-size:12px}

.products{top:687px;height:633px;background:var(--pale)}
.sec-title{position:absolute;left:0;width:1200px;text-align:center;font-size:56px;color:var(--navy)}
.products .sec-title{top:75px}
.card{position:absolute;width:260px;text-align:center}
.card .img{width:240px;height:207px;margin:0 auto;border-radius:40%;background:radial-gradient(circle,#d9a15a,#a4652a 55%,transparent 72%)}
.card h3{margin-top:30px;font-size:12px;font-weight:500;color:#333}
.card .price{margin-top:6px;font-size:14px;font-weight:600;color:var(--green)}
.products .btn{left:497px;top:515px;width:205px;height:42px;background:var(--green);color:#fff;font-size:14px}

.about{top:1320px;height:513px;background:var(--green);overflow:hidden}
.about .kicker{position:absolute;left:149px;top:100px;font-size:28px;color:#fff;text-decoration:underline}
.about h2{position:absolute;left:149px;top:140px;font-size:33px;line-height:36px;font-weight:700;color:#fff}
.about p{position:absolute;left:149px;width:380px;font-size:11.5px;line-height:21px;color:#f3fbe8;font-weight:300}
.about .btn{left:149px;top:390px;width:154px;height:41px;border:1.5px solid #fff;color:#fff;font-size:13px}
.about .photo{position:absolute;left:606px;top:124px;width:476px;height:307px;background:linear-gradient(135deg,#c9a070,#6d4a2c 55%,#1f3550);box-shadow:0 8px 20px rgba(0,0,0,.2)}
.about .cookies{position:absolute;left:0;top:321px;width:167px;height:192px;background:radial-gradient(ellipse at 30% 50%,#c98f4f,#9a6230 60%,transparent 75%)}

.team{top:1833px;height:610px;background:#fff}
.team .sec-title{top:70px}
.member{position:absolute;width:230px;text-align:center}
.member .portrait{width:190px;height:190px;margin:0 auto;border-radius:50%;background:linear-gradient(160deg,#e3e3e3,#bfbfbf);border:2px solid #eee}
.member h3{margin-top:30px;font-size:16px;font-weight:500;color:#333}
.member p{margin-top:8px;font-size:11.5px;line-height:21px;color:var(--muted);font-weight:300}
.member .btn{position:relative;margin:16px auto 0;width:98px;height:43px;background:var(--green);color:#fff;font-size:11px}
.arrow{position:absolute;top:265px}

.news{top:2443px;height:498px;background:var(--grey);overflow:hidden}
.news .photo{position:absolute;left:0;top:0;width:650px;height:498px;background:linear-gradient(150deg,#fff,#f3efe9 45%,#e8e3dc);clip-path:polygon(0 0,650px 0,550px 498px,0 498px)}
.news .stack{position:absolute;left:200px;top:45px;width:380px;height:390px;border-radius:40%;background:radial-gradient(ellipse,#d9a264,#a86b33 55%,transparent 72%)}
.news .kicker{position:absolute;left:674px;top:90px;font-size:24px;color:var(--navy);text-decoration:underline}
.news h2{position:absolute;left:674px;top:125px;font-size:33px;line-height:36px;font-weight:700;color:var(--navy)}
.news .date{position:absolute;left:674px;top:216px;font-size:11px;color:var(--green);font-weight:500}
.news p{position:absolute;left:674px;top:246px;width:390px;font-size:11.5px;line-height:21px;color:var(--muted);font-weight:300}
.news .btn{left:674px;top:361px;width:152px;height:41px;border:1.5px solid #777;color:var(--navy);font-size:13px}

.contact{top:2941px;height:475px;background:linear-gradient(90deg,rgba(20,20,20,.8),rgba(30,25,20,.6)),linear-gradient(120deg,#5a3f28,#2a2018 50%,#6c5038)}
.contact .sec-title{top:70px;color:#fff;font-size:54px}
.field{position:absolute;border:1.5px solid #fff;border-radius:22px;color:#ddd;font-size:12px;padding:10px 22px}
.contact .btn{left:307px;top:365px;width:586px;height:37px;background:var(--green);color:#fff;font-size:11px}

.site-footer{top:3416px;height:389px;background:var(--footer)}
.site-footer .brand{left:0;width:1200px;top:72px;justify-content:center}
.social{position:absolute;top:196px;left:458px;display:flex;gap:20px}
.social span{width:56px;height:56px;border-radius:50%;background:#2a3035}
.social span.on{background:#3fae4a}
.fnav{position:absolute;top:316px;width:1200px;display:flex;justify-content:center;gap:32px;font-size:12px;color:#ddd}
.copy{position:absolute;top:350px;width:1200px;text-align:center;font-size:11px;color:#ddd}
</style>
</head>
<body>

<header class="topbar">
  <div class="links"><span>My Account</span><span>Cart</span></div>
</header>

<header class="site-header">
  <div class="brand"><div class="mark"></div><div class="name">GRANA</div></div>
  <div class="phone">
    <div class="ic"><svg width="14" height="14" viewBox="0 0 24 24"><path d="M6.6 10.8a15 15 0 0 0 6.6 6.6l2.2-2.2c.3-.3.7-.4 1-.2 1.1.4 2.3.6 3.6.6.6 0 1 .4 1 1V20c0 .6-.4 1-1 1A17 17 0 0 1 3 4c0-.6.4-1 1-1h3.5c.6 0 1 .4 1 1 0 1.3.2 2.5.6 3.6.1.3 0 .7-.2 1z" fill="#7a9a0a"/></svg></div>
    +1-555-0142-377
  </div>
  <nav class="nav">
    <a class="active">Home</a><a>About</a><a>Product</a><a>Team</a><a>News</a><a>Footer</a><a>Contact</a>
  </nav>
</header>

<section class="hero">
  <div class="photo" role="img" aria-label="Baker taking notes beside a laptop with a tray of muffins"></div>
  <div class="loaf" role="img" aria-label="Loaf of bread with wheat ears"></div>
  <div class="kicker script">The Products</div>
  <h1>Local bakery</h1>
  <p>There are many variations of passages of Lorem Ipsum available, but the majority have suffered alteration</p>
  <a class="btn">SHOP NOW</a>
</section>

<section class="products">
  <h2 class="sec-title script">Our Product</h2>
  <div class="card" style="left:192px;top:185px"><div class="img" role="img" aria-label="Basket of muffins"></div><h3>BAKERY PRODUCT</h3><div class="price">$15.99</div></div>
  <div class="card" style="left:498px;top:185px"><div class="img" role="img" aria-label="Croissants on a cloth"></div><h3>BAKERY PRODUCT</h3><div class="price">$15.99</div></div>
  <div class="card" style="left:767px;top:185px"><div class="img" role="img" aria-label="Stack of cream-filled cookies"></div><h3>BAKERY PRODUCT</h3><div class="price">$15.99</div></div>
  <a class="btn">More Product</a>
</section>

<section class="about">
  <div class="cookies" role="img" aria-label="Stacked cookies"></div>
  <div class="kicker script">About US</div>
  <h2>Food From Local<br>Suppliers</h2>
  <p style="top:235px">Lorem Ipsum is simply dummy text of the printing and typesetting industry. Lorem Ipsum has been the industry's standard dummy text ever since the 1500s,</p>
  <p style="top:315px">when an unknown printer took a galley of type and scrambled it to make a type specimen book</p>
  <a class="btn">Read More</a>
  <div class="photo" role="img" aria-label="Two bakers holding a tray of fresh bread in a bakery"></div>
</section>

<section class="team">
  <h2 class="sec-title script">Our Team</h2>
  <svg class="arrow" style="left:174px" width="16" height="24" viewBox="0 0 16 24"><path d="M12 3 4 12l8 9" fill="none" stroke="#0f2a4a" stroke-width="2.5"/></svg>
  <svg class="arrow" style="left:1010px" width="16" height="24" viewBox="0 0 16 24"><path d="m4 3 8 9-8 9" fill="none" stroke="#0f2a4a" stroke-width="2.5"/></svg>
  <div class="member" style="left:231px;top:175px"><div class="portrait" role="img" aria-label="Portrait of team member"></div><h3>Marta Lindqvist</h3><p>Lorem Ipsum is simply dummy text of the printing and typesetting industry. Lorem Ipsum has been the</p><a class="btn">MORE INFO</a></div>
  <div class="member" style="left:482px;top:175px"><div class="portrait" role="img" aria-label="Portrait of team member"></div><h3>Rosa Delmar</h3><p>Lorem Ipsum is simply dummy text of the printing and typesetting industry. Lorem Ipsum has been the</p><a class="btn">MORE INFO</a></div>
  <div class="member" style="left:738px;top:175px"><div class="portrait" role="img" aria-label="Portrait of team member"></div><h3>Marta Lindqvist</h3><p>Lorem Ipsum is simply dummy text of the printing and typesetting industry. Lorem Ipsum has been the</p><a class="btn">MORE INFO</a></div>
</section>

<section class="news">
  <div class="photo"></div>
  <div class="stack" role="img" aria-label="Stack of cream-filled chocolate chip cookies"></div>
  <div class="kicker script">News</div>
  <h2>Food From Local<br>Suppliers</h2>
  <div class="date">24.10.2019</div>
  <p>Lorem Ipsum is simply dummy text of the printing and typesetting industry. Lorem Ipsum has been the industry's standard dummy text ever since the combined with a handful of model sentence structures, to generate Lorem Ipsum which</p>
  <a class="btn">Read More</a>
</section>

<section class="contact" role="img" aria-label="Bakery counter with shelves of bread and two staff members">
  <h2 class="sec-title script">Get in Touch</h2>
  <div class="field" style="left:307px;top:175px;width:283px;height:37px">Your Name</div>
  <div class="field" style="left:609px;top:175px;width:284px;height:37px">Your Email Address</div>
  <div class="field" style="left:307px;top:235px;width:586px;height:90px">Your Message</div>
  <a class="btn">SUBMIT HERE</a>
</section>

<footer class="site-footer">
  <div class="brand"><div class="mark"></div><div class="name">GRANA</div></div>
  <div class="social" aria-label="Social links"><span></span><span class="on"></span><span></span><span></span></div>
  <div class="fnav"><span>HOME</span><span>ABOUT</span><span>PRODUCT</span><span>TEAM</span><span>NEWS</span><span>FOOTER</span><span>CONTACT</span></div>
  <div class="copy">© 2019 bakery - All Rights Reserved. All Rights Reserved.</div>
</footer>

</body>
</html>
```